New Business Card Design Project

I'd like a business card design around the same modern style that I used on my website www.brisklanemaids.com
It's gonna be one of those round corners double-sided business cards with maybe a big logo on the front and all the info on the back of the card.

Contact Information for Business Card

Tomas Okafor
425-317-6840
www.brisklanemaids.com

www.facebook.com/BriskLaneMaidCare
www.intsgram.com/BriskLaneMaidCare

Requirements
Must have
• it needs to look elegant and modern

```html
<!DOCTYPE html>
<html lang="en">
<head>
<meta charset="utf-8">
<title>Brisk Lane Maid Care – Business Card</title>
<link rel="stylesheet" href="https://fonts.googleapis.com/css2?family=Work+Sans:wght@400;500;600&display=swap">
<style>
  :root {
    --page: #e9e9eb;
    --ink-dark: #2b2b2d;
    --ink-black: #1d1d1f;
    --brand-blue: #1e8fd8;
    --paper: #ffffff;
    --muted: #6c6c70;
    --light-text: #f2f2f2;
  }
  * { margin: 0; padding: 0; box-sizing: border-box; }
  html, body {
    width: 1200px; height: 715px; overflow: hidden;
    background: var(--page);
    font-family: "Work Sans", sans-serif;
  }
  .sheet {
    position: relative; width: 1200px; height: 715px;
    display: flex; align-items: center; justify-content: center; gap: 40px;
  }
  .card {
    position: relative; width: 540px; height: 309px;
    border-radius: 16px; overflow: hidden;
    box-shadow: 0 10px 28px rgba(0,0,0,.18);
  }
  .card-front {
    background: var(--ink-black);
    display: flex; align-items: center; justify-content: center;
  }
  .brand-mark {
    display: flex; align-items: center; gap: 14px;
    color: var(--brand-blue); font-weight: 600;
  }
  .brand-dot {
    width: 18px; height: 18px; border-radius: 50%;
    background: var(--brand-blue); flex: none;
  }
  .brand-name { line-height: 1.05; }
  .card-front .brand-name { font-size: 44px; }
  .card-back { background: var(--paper); }
  .card-back .backdrop { position: absolute; inset: 0; }
  .card-back .brand-mark { position: absolute; right: 34px; top: 52px; gap: 10px; }
  .card-back .brand-name { font-size: 30px; }
  .card-back .brand-dot { width: 13px; height: 13px; }
  .person { position: absolute; left: 30px; top: 84px; }
  .person-name {
    color: var(--brand-blue); font-size: 23px; font-weight: 500;
    letter-spacing: .5px; text-transform: uppercase;
  }
  .person-role { color: var(--muted); font-size: 13px; margin-top: 1px; }
  .contact-list {
    position: absolute; left: 30px; top: 164px; list-style: none;
    color: var(--light-text); font-size: 13px; line-height: 20px;
  }
  .contact-list li { display: flex; align-items: center; gap: 8px; }
  .contact-list svg { width: 10px; height: 10px; flex: none; }
  .address {
    position: absolute; right: 30px; bottom: 22px; text-align: right;
    color: var(--light-text); font-size: 15px; line-height: 22px; letter-spacing: .3px;
  }
</style>
</head>
<body>
<main class="sheet">
  <section class="card card-front">
    <div class="brand-mark">
      <span class="brand-dot"></span>
      <span class="brand-name">Brisk Lane<br>Maid Care</span>
    </div>
  </section>

  <section class="card card-back">
    <svg class="backdrop" viewBox="0 0 540 309" preserveAspectRatio="none" aria-hidden="true">
      <polygon points="0,140 205,140 215,150 540,208 540,309 0,309" fill="#1e8fd8"/>
      <polygon points="0,146 203,146 213,156 540,214 540,309 0,309" fill="#2b2b2d"/>
    </svg>

    <div class="brand-mark">
      <span class="brand-dot"></span>
      <span class="brand-name">Brisk Lane<br>Maid Care</span>
    </div>

    <div class="person">
      <p class="person-name">Tomas Okafor</p>
      <p class="person-role">Director</p>
    </div>

    <ul class="contact-list">
      <li>
        <svg viewBox="0 0 10 10"><path d="M2 0.5 L3.6 2.6 L2.8 3.6 Q4 6 6.4 7.2 L7.4 6.4 L9.5 8 L8.4 9.5 Q3.5 9 0.5 1.6 Z" fill="#1e8fd8"/></svg>
        425-317-6840
      </li>
      <li>
        <svg viewBox="0 0 10 10"><rect x="0.6" y="2" width="8.8" height="6" fill="none" stroke="#1e8fd8" stroke-width="1.2"/><path d="M0.6 2 L5 5.6 L9.4 2" fill="none" stroke="#1e8fd8" stroke-width="1.2"/></svg>
        info@brisklanemaids.com
      </li>
      <li>
        <svg viewBox="0 0 10 10"><circle cx="5" cy="5" r="4.2" fill="none" stroke="#1e8fd8" stroke-width="1.2"/><path d="M0.8 5 H9.2 M5 0.8 Q2.6 5 5 9.2 M5 0.8 Q7.4 5 5 9.2" fill="none" stroke="#1e8fd8" stroke-width="0.9"/></svg>
        www.brisklanemaids.com
      </li>
      <li>
        <svg viewBox="0 0 10 10"><rect x="1" y="1" width="8" height="8" fill="#1e8fd8"/></svg>
        /BriskLaneMaidCare
      </li>
      <li>
        <svg viewBox="0 0 10 10"><rect x="1" y="1" width="8" height="8" fill="#1e8fd8"/></svg>
        /BriskLaneMaidCare
      </li>
    </ul>

    <p class="address">2740 Harlow Creek Road<br>Oklahoma City, OK 73012</p>
  </section>
</main>
</body>
</html>
```